Cobalt Bridge Capital - Letterhead

We need letterhead options for our case funding company called Cobalt Bridge Capital. Here are some of the details:

Name - Cobalt Bridge Capital
Phone - (555) 214 - 9087
Address - 58 Harlow Lane
Suite 312
New York, NY 10482
Website - cobaltbridgecapital.example

```html
<!DOCTYPE html>
<html lang="en">
<head>
<meta charset="utf-8">
<title>Cobalt Bridge Capital – Letterhead</title>
<link rel="stylesheet" href="https://fonts.googleapis.com/css2?family=Open+Sans:wght@400;600&family=Lato:wght@400;700&display=swap">
<style>
  :root {
    --navy: #0f3150;
    --slate: #6f7f8c;
    --ink: #4a4a4a;
    --paper: #ffffff;
  }
  * { margin: 0; padding: 0; box-sizing: border-box; }
  html, body { width: 1040px; height: 1200px; overflow: hidden; background: var(--paper); }
  .letterhead {
    position: relative;
    width: 1040px;
    height: 1200px;
    font-family: "Open Sans", sans-serif;
    color: var(--ink);
    font-size: 16.5px;
  }
  .brand {
    position: absolute;
    top: 38px;
    right: 102px;
    display: flex;
    align-items: flex-end;
    gap: 12px;
  }
  .brand-dot {
    width: 80px; height: 80px;
    border-radius: 50%;
    background: var(--navy);
  }
  .brand-name {
    font-weight: 600;
    color: var(--navy);
    font-size: 16px;
    letter-spacing: 2px;
    line-height: 19px;
    text-transform: uppercase;
    margin-bottom: -34px;
  }
  .body {
    position: absolute;
    left: 97px;
    width: 840px;
  }
  .issue-date { top: 214px; }
  .recipient { top: 250px; line-height: 19px; font-style: normal; }
  .salutation { top: 356px; }
  .letter-text { top: 400px; }
  .letter-text p {
    text-align: justify;
    hyphens: auto;
    line-height: 27px;
    margin-bottom: 27px;
  }
  .closing { top: 814px; }
  .signatory { top: 884px; }
  .signatory-name { font-size: 19px; font-weight: 600; color: #333; }
  .signatory-title { margin-top: 4px; }
  .website {
    position: absolute;
    top: 1102px;
    left: 0; width: 1040px;
    text-align: center;
    font-family: "Lato", sans-serif;
    font-weight: 700;
    font-size: 17px;
    color: var(--navy);
  }
  .website span { font-weight: 400; }
  .contact-band {
    position: absolute;
    top: 1138px;
    left: 0;
    width: 930px;
    height: 50px;
    background: var(--navy);
    border-radius: 0 25px 25px 0;
    display: flex;
    align-items: center;
    justify-content: center;
    font-family: "Lato", sans-serif;
    font-size: 18px;
    color: #fff;
  }
  .contact-band b { font-weight: 700; margin-right: 6px; }
  .contact-band .divider { margin: 0 12px; }
  .band-dot {
    position: absolute;
    top: 1122px;
    left: 950px;
    width: 72px; height: 72px;
    border-radius: 50%;
    background: var(--slate);
  }
</style>
</head>
<body>
<main class="letterhead">
  <header class="brand">
    <span class="brand-dot"></span>
    <div class="brand-name">Cobalt<br>Bridge<br>Capital</div>
  </header>

  <p class="body issue-date">Issuing Date: May 5, 2018</p>
  <address class="body recipient">
    Name Of Employee Mr. XYZABC<br>
    Address of Employee<br>
    Address Line 2 etc..
  </address>
  <p class="body salutation">Dear Mr.XYZABC</p>

  <section class="body letter-text">
    <p>Lorem Ipsum has been the industry's standard dummy text ever since the 1500s, when an unknown printer took a galley of type and scrambled it to make a type specimen book. It has survived not only five centuries, but also the leap into electronic typesetting, remaining essentially unchanged. It was popularised in the 1960s with the release of Printwell sheets containing Lorem Ipsum passages, and more recently with desktop publishing software like Quillset Layout including versions of Lorem Ipsum.</p>
    <p>Lorem Ipsum is simply dummy text of the printing and typesetting industry. Lorem Ipsum has been the industry's standard dummy text ever since the 1500s, when an unknown printer took a galley of type and scrambled it to make a type specimen book.</p>
    <p>It has survived not only five centuries, but also the leap into electronic typesetting, remaining essentially unchanged. It was popularised in the 1960s with the release of Printwell sheets containing Lorem IpsumIpsum passages.</p>
  </section>

  <p class="body closing">Yours Sincerely</p>
  <div class="body signatory">
    <p class="signatory-name">Marcus Delaney</p>
    <p class="signatory-title">Managing Director</p>
  </div>

  <footer>
    <p class="website">www.<span>cobaltbridgecapital</span>.example</p>
    <div class="contact-band">
      <b>P:</b> (555) 214 - 9087<span class="divider">|</span>58 Harlow Lane , Suite 312 New York, NY 10482
    </div>
    <span class="band-dot"></span>
  </footer>
</main>
</body>
</html>
```